Thistlewood Candles, Hand-poured scented soy candles

Create a logo and label design to use on my vintage country farmhouse style, all natural, hand poured soy candle jars and apothecaries. Candles will be labeled in 4 different sizes so design must be adaptable, clean, simple, telegraphic and invoke interest in the product. Think Black lettering on white or black on kraft brown. Thistlewood is the area code for New Hampshire where we make them. The labels will need a prominent area for the scent of the candle to be listed that the eyes are drawn to. Primitive country in design? Use of state attractions? Jars are a square mason style 8 ounce and 16 ounce. Tarts are a clamshell. Lids are a 70-400 series 2.5" label area. Candles are white in a clear glass jar, black lids. There will be label design sizes of 3"x 2.5" 2.5" round, 1.5"x2.5"

Target Market(s)

primitive country, farmhouse, vintage, general home decor

Contact Information for Business Card

Thistlewood Candles, all natural soy candles, hand-poured in New Hampshire, logo, phone, address. Possibly match the main label.

Logo Text

Thistlewood Candles, all natural soy candles, hand-poured in New Hampshire, area for scent description and size of container.

Font styles to use
Serif
Script

Colors

Designer to choose colors to be used in the design.

Requirements
Must have
• simple and clean, country farmhouse with a bit of vintage thrown in. possibly multiple fonts to distinguish info from scent name
Nice to have
• at this time I am open to suggestions
• Prefer scent names or brand name in an older script?
• older copperplate/Spencerian?
Should not have
• cluttered, busy, too modern, multiple colors

```html
<!DOCTYPE html>
<html lang="en">
<head>
<meta charset="utf-8">
<title>Thistlewood Candles – Label System</title>
<link rel="stylesheet" href="https://fonts.googleapis.com/css2?family=Playfair+Display:wght@600&family=Roboto+Slab:wght@400;700&display=swap">
<style>
  :root {
    --ink: #333132;
    --gold: #cbb888;
    --panel: #e6e7e9;
    --paper: #ffffff;
    --serif-display: "Playfair Display", serif;
    --slab: "Roboto Slab", serif;
  }
  * { box-sizing: border-box; margin: 0; padding: 0; }
  html, body { width: 1200px; height: 1200px; overflow: hidden; background: var(--paper); }
  .sheet { position: relative; width: 1200px; height: 1200px; background: var(--paper); }
  .sizes-panel { position: absolute; left: 0; top: 0; width: 658px; height: 1200px; background: var(--panel); }

  .dimensions { position: absolute; left: 0; top: 0; width: 1200px; height: 1200px; pointer-events: none; }
  .dimensions line { stroke: var(--ink); stroke-width: 2.5; }
  .dimensions text { font-family: var(--serif-display); font-weight: 600; font-size: 19px; fill: var(--ink); letter-spacing: 1px; }

  .label { position: absolute; background: var(--paper); border: 5px solid var(--ink); }
  .label__band { position: absolute; inset: 3px; border: 4px solid var(--gold); border-radius: inherit; }
  .label__stitch { position: absolute; inset: 4px; border: 1.2px dashed var(--gold); border-radius: inherit; }
  .label--tall { left: 242px; top: 170px; width: 146px; height: 234px; border-radius: 20px; }
  .label--wide { left: 168px; top: 477px; width: 279px; height: 234px; border-radius: 20px; }
  .label--round { left: 190px; top: 794px; width: 236px; height: 236px; border-radius: 50%; }

  .line { position: absolute; left: 0; right: 0; text-align: center; color: var(--ink); white-space: nowrap; }
  .tagline { font-family: var(--serif-display); font-weight: 600; letter-spacing: -0.3px; }
  .subline { font-family: var(--slab); font-weight: 700; letter-spacing: 0.6px; }
  .brand-name { font-family: var(--slab); font-weight: 700; line-height: 1.05; }

  .ornament { position: absolute; height: 14px; background: var(--gold); border-radius: 7px; opacity: 0.85; }

  .label--tall .tagline { top: 52px; font-size: 8px; }
  .label--tall .brand-name { top: 92px; font-size: 18px; }
  .label--tall .subline { top: 168px; font-size: 6.5px; }

  .label--wide .tagline { top: 28px; font-size: 9px; }
  .label--wide .brand-name { top: 78px; font-size: 27px; }
  .label--wide .subline { top: 168px; font-size: 8.5px; }

  .label--round .brand-name { top: 74px; font-size: 22px; }
  .label--round .subline { top: 170px; font-size: 8.5px; }
  .arc-text { position: absolute; left: 0; top: 0; width: 226px; height: 226px; }
  .arc-text text { font-family: var(--serif-display); font-weight: 600; font-size: 10px; fill: var(--ink); }

  .showcase { position: absolute; left: 700px; top: 318px; width: 460px; }
  .showcase .tagline { position: static; font-size: 31px; letter-spacing: -0.6px; }
  .showcase .brand-name { position: static; margin-top: 88px; font-size: 64px; color: var(--ink); }
  .showcase .subline { position: static; margin-top: 70px; font-size: 30px; letter-spacing: 2.5px; }
</style>
</head>
<body>
<main class="sheet">
  <section class="sizes-panel" aria-label="Label sizes">

    <div class="label label--tall">
      <div class="label__band"><div class="label__stitch"></div></div>
      <div class="ornament" style="left:28px; top:24px; width:80px;" role="img" aria-label="Gold scroll flourish"></div>
      <p class="line tagline">hand poured in New Hampshire</p>
      <p class="line brand-name">Thistlewood<br>Candles</p>
      <p class="line subline">all natural soy candles</p>
      <div class="ornament" style="left:28px; top:188px; width:80px;" role="img" aria-label="Gold scroll flourish"></div>
    </div>

    <div class="label label--wide">
      <div class="label__band"><div class="label__stitch"></div></div>
      <div class="ornament" style="left:26px; top:28px; width:38px; height:11px;" role="img" aria-label="Gold scroll flourish"></div>
      <p class="line tagline">hand poured in New Hampshire</p>
      <div class="ornament" style="left:206px; top:28px; width:38px; height:11px;" role="img" aria-label="Gold scroll flourish"></div>
      <p class="line brand-name">Thistlewood<br>Candles</p>
      <p class="line subline">all natural soy candles</p>
      <div class="ornament" style="left:87px; top:187px; width:96px;" role="img" aria-label="Gold scroll flourish"></div>
    </div>

    <div class="label label--round">
      <div class="label__band"><div class="label__stitch"></div></div>
      <svg class="arc-text" viewBox="0 0 226 226" aria-label="hand poured in New Hampshire">
        <defs><path id="arc-top" d="M 38 113 A 75 75 0 0 1 188 113"/></defs>
        <text><textPath href="#arc-top" startOffset="50%" text-anchor="middle">hand poured in New Hampshire</textPath></text>
      </svg>
      <p class="line brand-name">Thistlewood<br>Candles</p>
      <p class="line subline">all natural soy candles</p>
      <div class="ornament" style="left:66px; top:186px; width:94px; height:12px;" role="img" aria-label="Gold scroll flourish"></div>
    </div>

    <svg class="dimensions" viewBox="0 0 1200 1200" aria-hidden="true">
      <line x1="404" y1="175" x2="404" y2="399"/>
      <line x1="396" y1="175" x2="412" y2="175"/>
      <line x1="396" y1="399" x2="412" y2="399"/>
      <text x="412" y="288">2.5"</text>
      <line x1="248" y1="420" x2="383" y2="420"/>
      <line x1="248" y1="412" x2="248" y2="429"/>
      <line x1="383" y1="412" x2="383" y2="429"/>
      <text x="316" y="447" text-anchor="middle">1.5"</text>

      <line x1="465" y1="482" x2="465" y2="707"/>
      <line x1="456" y1="482" x2="474" y2="482"/>
      <line x1="456" y1="707" x2="474" y2="707"/>
      <text x="473" y="597">2.5"</text>
      <line x1="173" y1="728" x2="443" y2="728"/>
      <line x1="173" y1="719" x2="173" y2="738"/>
      <line x1="443" y1="719" x2="443" y2="738"/>
      <text x="307" y="756" text-anchor="middle">3"</text>

      <line x1="465" y1="800" x2="465" y2="1025"/>
      <line x1="368" y1="800" x2="474" y2="800"/>
      <line x1="368" y1="1025" x2="474" y2="1025"/>
      <text x="474" y="913">ø 2.5"</text>
    </svg>
  </section>

  <section class="showcase" aria-label="Primary mark">
    <p class="line tagline">hand poured in New Hampshire</p>
    <p class="line brand-name">Thistlewood<br>Candles</p>
    <p class="line subline">all natural soy candles</p>
  </section>
</main>
</body>
</html>
```